Ondas Tierra - Stationery and Presentation Materials
Biz card, letterhead, envelope, presentation folder
Bright & Fun-filled
Martin Coble
E.S.
Tel. +503.2417.8836
Cel. +503.7396.1052
U.S. +1.800.555.0147 x3061
U.S.
ondastierra.led@correoplano.com
PLEASE, DON'T POST EMAIL IN DRAFTS.
--The business is rental of large LED screens for visuals, which are made of thousands of tiny lights.
---Please give a range of crazy/abstract as well as aggressive but traditional/corporate concepts for all items in subtitle.
---The presentation folder is to digitally insert fotos later for printing. Borders are key. A CD will be included, on a plastic peg anywhere in the folder, and CD design must blend with folder graphics on the point where CD sits.
Minimal.
---try wrap-around logo
----1 "wild concept" if anyone is willing - background is very tiny, SHINING, white lights (almost pixel-looking), with the logo symbol on top.

```html
<!DOCTYPE html>
<html lang="es">
<head>
<meta charset="utf-8">
<title>Ondas Tierra – Tarjetas de presentación</title>
<link href="https://fonts.googleapis.com/css2?family=Nunito:wght@800&family=Lato:wght@400;700&display=swap" rel="stylesheet">
<style>
  :root{
    --page:#efe7da;
    --white:#ffffff;
    --red:#e8322f;
    --orange:#f7941d;
    --amber:#fbb040;
    --purple:#3a2a8c;
    --violet:#5b3fb3;
    --blue:#2a6fd6;
  }
  *{margin:0;padding:0;box-sizing:border-box}
  html,body{width:1200px;height:816px;overflow:hidden;background:var(--page)}
  .canvas{position:relative;width:1200px;height:816px}
  .card{position:absolute;width:432px;height:248px;border-radius:18px;overflow:hidden;box-shadow:0 6px 14px rgba(0,0,0,.18)}
  .card--front{left:149px;top:137px;background:var(--white)}
  .card--back-warm{left:605px;top:137px;background:radial-gradient(ellipse at 45% 55%,var(--amber) 0%,var(--orange) 35%,var(--red) 80%)}
  .card--back-cool{left:379px;top:496px;background:radial-gradient(ellipse at 45% 50%,var(--blue) 0%,var(--violet) 45%,var(--purple) 85%)}
  .brand{position:absolute;display:flex;align-items:center;gap:12px;font-family:"Nunito",sans-serif;font-weight:800;white-space:nowrap;line-height:1}
  .brand__mark{display:block;flex:none}
  .card--front .brand{left:16px;top:14px;font-size:32px;color:var(--red)}
  .card--front .brand__mark{width:62px;height:62px;background:var(--red)}
  .card--back-warm .brand,.card--back-cool .brand{left:50%;top:50%;transform:translate(-50%,-50%);font-size:44px;color:var(--white)}
  .card--back-warm .brand__mark,.card--back-cool .brand__mark{width:72px;height:72px;background:var(--white)}
  .holder{position:absolute;left:14px;top:152px;font-family:"Lato",sans-serif;font-weight:700;font-size:18px;color:var(--red)}
  .wave{position:absolute;left:0;bottom:0;width:432px;height:120px}
  .contact{position:absolute;right:18px;bottom:16px;text-align:right;font-family:"Lato",sans-serif;font-size:9.5px;line-height:13px;color:var(--white);list-style:none}
</style>
</head>
<body>
<main class="canvas">
  <section class="card card--front" aria-label="Tarjeta frontal">
    <div class="brand"><span class="brand__mark"></span>Ondas Tierra</div>
    <p class="holder">Martin Coble</p>
    <svg class="wave" viewBox="0 0 432 120" preserveAspectRatio="none" aria-hidden="true">
      <defs>
        <linearGradient id="waveFill" x1="0" y1="0" x2="1" y2="0">
          <stop offset="0" stop-color="#e8322f"/>
          <stop offset=".5" stop-color="#f26a22"/>
          <stop offset="1" stop-color="#f7941d"/>
        </linearGradient>
      </defs>
      <path d="M0 44 C120 74 240 14 432 20 L432 120 L0 120 Z" fill="#2a6fd6"/>
      <path d="M0 51 C120 81 240 21 432 27 L432 120 L0 120 Z" fill="url(#waveFill)"/>
    </svg>
    <ul class="contact">
      <li>E.S.</li>
      <li>Tel. +503.2417.8836</li>
      <li>Cel. +503.7396.1052</li>
      <li>U.S. +1.800.555.0147 x3061</li>
      <li>U.S. +1.772.555.0193</li>
    </ul>
  </section>

  <section class="card card--back-warm" aria-label="Reverso cálido">
    <div class="brand"><span class="brand__mark"></span>Ondas Tierra</div>
  </section>

  <section class="card card--back-cool" aria-label="Reverso frío">
    <div class="brand"><span class="brand__mark"></span>Ondas Tierra</div>
  </section>
</main>
</body>
</html>
```